Torvaline business cards

Need fresh design for our business cards. Logo must be specific, we are open for everything else.

Contact Information for Business Card

phrase "GMP & JANITORIAL SERVICES" should be used as main point of card

Colors
3176b5
3276b5
85acd3
cedeed
ffffff
0292cd
33a6d7
85cae6
cee9f5

Requirements
Must have
• The logo
Should not have
• crowded designs

```html
<!DOCTYPE html>
<html lang="en">
<head>
<meta charset="utf-8">
<title>Torvaline Business Cards</title>
<link rel="stylesheet" href="https://fonts.googleapis.com/css2?family=Roboto:wght@400;500;700&display=swap">
<style>
  :root {
    --page-bg: #ececec;
    --card-white: #f7f7f7;
    --brand-blue: #1b7dc1;
    --back-blue: #1f87c8;
    --text-grey: #4a4a4a;
    --divider: #9a9a9a;
    --white: #ffffff;
  }
  html, body {
    margin: 0;
    padding: 0;
    width: 1125px;
    height: 1200px;
    overflow: hidden;
    background: var(--page-bg);
    font-family: "Roboto", Arial, sans-serif;
  }
  .canvas {
    position: relative;
    width: 1125px;
    height: 1200px;
  }
  .card {
    position: absolute;
    left: 150px;
    width: 825px;
    height: 471px;
    box-sizing: border-box;
  }
  .card-front {
    top: 98px;
    background: var(--card-white);
  }
  .card-back {
    top: 631px;
    background: var(--back-blue);
  }
  .back-fill {
    position: absolute;
    inset: 0;
    background: var(--back-blue);
  }
  .brand-name {
    position: absolute;
    margin: 0;
    font-weight: 400;
    line-height: 1;
    white-space: nowrap;
  }
  .card-front .brand-name {
    left: 98px;
    top: 211px;
    font-size: 46px;
    letter-spacing: 9px;
    color: var(--brand-blue);
  }
  .card-back .brand-name {
    left: 289px;
    top: 299px;
    font-size: 66px;
    letter-spacing: 15px;
    color: var(--white);
  }
  .brand-tagline {
    position: absolute;
    margin: 0;
    font-weight: 400;
    line-height: 1;
    white-space: nowrap;
  }
  .card-front .brand-tagline {
    right: 402px;
    top: 264px;
    font-size: 10px;
    letter-spacing: 2px;
    color: var(--brand-blue);
  }
  .card-back .brand-tagline {
    right: 58px;
    top: 361px;
    font-size: 14px;
    letter-spacing: 2.6px;
    color: var(--white);
  }
  .divider {
    position: absolute;
    left: 450px;
    top: 93px;
    width: 2px;
    height: 289px;
    background: linear-gradient(to bottom, transparent, var(--divider) 15%, var(--divider) 85%, transparent);
  }
  .contact {
    position: absolute;
    left: 484px;
    top: 112px;
    color: var(--text-grey);
  }
  .contact-name {
    margin: 0;
    font-size: 31px;
    font-weight: 500;
    color: var(--brand-blue);
    line-height: 1.05;
  }
  .contact-role {
    margin: 0 0 16px;
    font-size: 20px;
    font-weight: 500;
    color: var(--text-grey);
  }
  .contact-address {
    margin: 0 0 10px;
    font-size: 20px;
    line-height: 25px;
    font-style: normal;
  }
  .contact-lines {
    list-style: none;
    margin: 0;
    padding: 0;
    font-size: 20px;
    line-height: 25px;
  }
  .contact-lines li {
    display: flex;
    align-items: center;
    gap: 12px;
  }
  .contact-lines svg {
    width: 18px;
    height: 18px;
    fill: var(--brand-blue);
    flex: none;
  }
  .website {
    position: absolute;
    left: 300px;
    top: 383px;
    margin: 0;
    font-size: 21px;
    line-height: 1;
    letter-spacing: 17px;
    color: var(--white);
    white-space: nowrap;
  }
</style>
</head>
<body>
<main class="canvas">

  <section class="card card-front" aria-label="Card front">
    <p class="brand-name">TORVALINE</p>
    <p class="brand-tagline">GMP &amp; JANITORIAL SERVICES</p>
    <div class="divider"></div>
    <div class="contact">
      <h1 class="contact-name">Daniel Reyes</h1>
      <p class="contact-role">President</p>
      <address class="contact-address">4120 Larkspur Way<br>Fairbrook, Alaska 28461</address>
      <ul class="contact-lines">
        <li>
          <svg viewBox="0 0 24 24" aria-hidden="true"><path d="M6.6 10.8a15.1 15.1 0 0 0 6.6 6.6l2.2-2.2c.3-.3.7-.4 1-.2 1.1.4 2.3.6 3.6.6.6 0 1 .4 1 1V20c0 .6-.4 1-1 1A17 17 0 0 1 3 4c0-.6.4-1 1-1h3.5c.6 0 1 .4 1 1 0 1.3.2 2.5.6 3.6.1.3 0 .7-.2 1z"/></svg>
          <span>555-214-7830</span>
        </li>
        <li>
          <svg viewBox="0 0 24 24" aria-hidden="true"><path d="M7 1h10a2 2 0 0 1 2 2v18a2 2 0 0 1-2 2H7a2 2 0 0 1-2-2V3a2 2 0 0 1 2-2zm0 3v14h10V4zm5 15.5a1 1 0 1 0 0 2 1 1 0 0 0 0-2z"/></svg>
          <span>555-619-2047</span>
        </li>
        <li>
          <svg viewBox="0 0 24 24" aria-hidden="true"><path d="M6 2h12v6H6zM3 9h18a2 2 0 0 1 2 2v6h-4v5H5v-5H1v-6a2 2 0 0 1 2-2zm4 6v5h10v-5z"/></svg>
          <span>555-338-4152</span>
        </li>
        <li>
          <svg viewBox="0 0 24 24" aria-hidden="true"><path d="M2 5h20v14H2zm2 2v.5l8 5 8-5V7zm0 2.8V17h16V9.8l-8 5z"/></svg>
          <span>info@torvaline.com</span>
        </li>
      </ul>
    </div>
  </section>

  <section class="card card-back" aria-label="Card back">
    <div class="back-fill" role="img" aria-label="Blue background with a repeating pattern of concentric circles"></div>
    <p class="brand-name">TORVALINE</p>
    <p class="brand-tagline">GMP &amp; JANITORIAL SERVICES</p>
    <p class="website">www.torvaline.com</p>
  </section>

</main>
</body>
</html>
```